IT Company Business Card design

Brisk Node is a new computer solutions business focusing on setting up servers and computer systems for small to medium sized businesses.

A business client will either request a solution, or support for a current system and we will turn up on site to provide these services.

We are bast in Christchurch, New Zealand.

We are looking for unique business card's that stand out and show off the business in a professional light.

Open to all idea's etc.

Industry/Entity Type

Computer

Requirements
Must have
• Business Logo (AI file attached)
Employee Name
Business title
Business landline number
Cell phone number
Email
Web URL
Nice to have
• Could be nice to have some keywords (possibly on the back) such as:

Business IT solutions
Network installations
Phone solutions
Server management
Software diagnostics

The above is not needed, just an idea.

```html
<!DOCTYPE html>
<html lang="en">
<head>
<meta charset="utf-8">
<title>Brisk Node – Business Card</title>
<link href="https://fonts.googleapis.com/css2?family=Cabin:wght@400&family=Open+Sans:wght@400&family=Arimo:wght@400&display=swap" rel="stylesheet">
<style>
  :root {
    --page-bg: #ffffff;
    --card-bg: #f8f9fa;
    --card-edge: #ececec;
    --ink: #0b0b0b;
    --ink-soft: #333333;
    --brand-blue: #1a6fc4;
    --divider: #9a9a9a;
  }
  * { margin: 0; padding: 0; box-sizing: border-box; }
  html, body {
    width: 1200px;
    height: 1000px;
    overflow: hidden;
    background: var(--page-bg);
  }
  .canvas {
    position: relative;
    width: 1200px;
    height: 1000px;
  }
  .card {
    position: absolute;
    left: 157px;
    top: 189px;
    width: 874px;
    height: 614px;
    background: var(--card-bg);
    border: 1px solid var(--card-edge);
    color: var(--ink);
  }
  .brand-mark {
    position: absolute;
    left: 303px;
    top: 39px;
  }
  .brand-divider {
    position: absolute;
    left: 495px;
    top: 44px;
    width: 2px;
    height: 172px;
    background: linear-gradient(to bottom, transparent, var(--divider) 30%, var(--divider) 70%, transparent);
  }
  .brand-name {
    position: absolute;
    right: 34px;
    top: 98px;
    font-family: "Cabin", sans-serif;
    font-weight: 400;
    font-size: 54px;
    letter-spacing: 5px;
    line-height: 1;
    white-space: nowrap;
  }
  .brand-url {
    position: absolute;
    right: 41px;
    top: 160px;
    font-family: "Arimo", sans-serif;
    font-size: 25px;
    line-height: 1;
    white-space: nowrap;
  }
  .person-name,
  .person-title,
  .person-mobile {
    position: absolute;
    left: 32px;
    line-height: 1;
    white-space: nowrap;
    font-weight: 400;
  }
  .person-name {
    top: 328px;
    font-family: "Cabin", sans-serif;
    font-size: 120px;
  }
  .person-title {
    top: 473px;
    font-family: "Cabin", sans-serif;
    font-size: 66px;
  }
  .person-mobile {
    top: 531px;
    font-family: "Open Sans", sans-serif;
    font-size: 48px;
  }
  .contact-extra {
    position: absolute;
    right: 41px;
    bottom: 40px;
    text-align: right;
    font-family: "Arimo", sans-serif;
    font-size: 24px;
    line-height: 1.35;
    color: var(--ink-soft);
    white-space: nowrap;
  }
</style>
</head>
<body>
  <main class="canvas">
    <section class="card">
      <svg class="brand-mark" width="170" height="170" viewBox="0 0 170 170" aria-hidden="true">
        <circle cx="85" cy="85" r="84" fill="var(--brand-blue)"/>
      </svg>
      <div class="brand-divider"></div>
      <div class="brand-name">BRISK NODE</div>
      <div class="brand-url">www.brisknode.co.nz</div>

      <h1 class="person-name">Sam Tarrant</h1>
      <p class="person-title">Senior Technician</p>
      <p class="person-mobile">021 478 302</p>

      <div class="contact-extra">
        <p class="contact-landline">Office 03 348 5710</p>
        <p class="contact-email">sam@brisknode.co.nz</p>
      </div>
    </section>
  </main>
</body>
</html>
```